Harbourgate Earthmoving – Website Design Brief

Web Design Brief

We are seeking a web designer to build a modern, responsive website for Harbourgate Earthmoving, a Sydney-based earthworks and excavation company.

2. Project Goal
- Build a professional, easy-to-navigate website that:
- Showcases HGE’s capabilities and past projects
- Attracts residential and commercial developers
- Builds credibility and encourages enquiries

3. Target Audience
- Residential developers and home builders
- Commercial construction firms
- Project managers seeking reliable excavation & plant hire services

4. Services to Highlight
- Bulk Excavation
- Detailed Excavation
- Demolition
- Shoring
- Plant Hire

5. Brand Style & Tone
- Clean, bold, and modern
- Professional with a “we get the job done” attitude
- Colors: Lime Green + Concrete Grey (from logo)
- Fonts: Match the modern, rounded, bold typeface in the logo
- Imagery: Showcase big machines, on-site work, before & after shots

6. Website Pages
Recommended structure:
- Home – Quick intro, project highlights, CTA
- About Us – Team story, mission, safety focus
- Services – Separate sections for each core service
- Projects – Case studies or photo gallery
- Plant Hire – Machines available, specs/photos
- Contact – Form + map + details

7. Assets Provided
- Logo (both long + stacked formats)
- Project photos. More can be provided if required.
- Copy: To be drafted

8. Deliverables
Responsive website (desktop/mobile/tablet)
- SEO-ready structure
- CMS (WordPress) for future edits
- Google Maps integration, job enquiry form

Target Market(s)

Target Audience Residential developers and home builders Commercial construction firms Project managers seeking reliable excavation & plant hire services

Industry/Entity Type

Construction

Number of Pages Required

1 page

Requirements
Must have
• Build a professional, easy-to-navigate website that: Showcases HGE’s capabilities and past projects Attracts residential and commercial developers Builds credibility and encourages enquiries
Nice to have
• All provided in the Description
Should not have

```html
<!DOCTYPE html>
<html lang="en">
<head>
<meta charset="utf-8">
<title>Harbourgate Earthmoving</title>
<link rel="stylesheet" href="https://fonts.googleapis.com/css2?family=Michroma&family=Inter+Tight:wght@400;500;600&display=swap">
<style>
:root{
  --lime:#7cbd36;
  --lime-dark:#5aa72c;
  --grey:#8b8b8b;
  --grey-dark:#6f6f6f;
  --ink:#222;
  --text:#444;
  --muted:#777;
  --white:#fff;
  --line:#d5d5d5;
}
*{box-sizing:border-box;margin:0;padding:0}
html,body{width:1200px;height:4335px;overflow:hidden}
body{font-family:"Inter Tight",Arial,sans-serif;color:var(--text);background:var(--white);position:relative}
.display{font-family:"Michroma",sans-serif;text-transform:uppercase;letter-spacing:4px;color:var(--ink)}
.display .accent{color:var(--lime)}
.rule{width:72px;height:4px;background:var(--lime);border-radius:2px}
.photo{display:block}

/* header */
.topbar{height:108px;border-top:4px solid var(--lime);display:flex;align-items:center;padding-left:116px}
.brand{font-family:"Inter Tight",sans-serif;font-weight:600;font-size:17px;line-height:1.15;color:var(--lime);width:170px;text-transform:uppercase;letter-spacing:1px}
.contact-strip{display:flex;margin-left:20px}
.contact-item{display:flex;align-items:center;gap:12px;padding:0 28px;border-left:1px solid var(--line);height:60px}
.contact-item:first-child{border-left:none}
.contact-item svg{width:34px;height:34px;flex:none}
.contact-item b{display:block;font-weight:500;font-size:16px;color:var(--ink)}
.contact-item span{font-size:13px;color:var(--muted)}
.navbar{height:60px;background:var(--grey);display:flex;align-items:center;position:relative}
.nav-links{display:flex;list-style:none;margin-left:106px}
.nav-links li{color:var(--white);font-size:14px;padding:0 25px;border-left:1px solid rgba(255,255,255,.6)}
.nav-links li:first-child{border-left:none;padding-left:16px}
.quick-quote{position:absolute;right:0;top:0;height:60px;width:430px;background:var(--lime);display:flex;align-items:center;padding-left:4px;color:var(--white)}
.quick-quote .dot{width:42px;height:42px;border-radius:50%;background:var(--white);display:flex;align-items:center;justify-content:center;margin-right:10px}
.quick-quote small{display:block;font-size:9px}
.quick-quote b{font-weight:500;font-size:17px}

/* hero */
.hero{height:520px;position:relative;text-align:center;overflow:hidden}
.hero .photo{position:absolute;inset:0;width:100%;height:100%;background:linear-gradient(180deg,#a9acab 0%,#8d9290 40%,#5c5f58 70%,#4b3f36 100%)}
.hero-inner{position:relative;padding-top:58px}
.hero h1{font-family:"Michroma",sans-serif;font-weight:400;font-size:26px;letter-spacing:7px;color:#111;text-transform:uppercase}
.hero .name{font-family:"Michroma",sans-serif;font-size:37px;letter-spacing:2px;color:var(--lime);margin-top:30px;white-space:nowrap}
.btn{display:inline-block;border-radius:12px;color:var(--white);font-size:16px}
.hero .btn{background:var(--lime);padding:13px 42px;margin-top:34px}

/* services */
.services{height:1070px;position:relative}
.section-title{text-align:center;font-size:28px}
.services .section-title{padding-top:110px}
.services .rule{margin:16px auto 0}
.service-row{position:absolute;top:207px;left:100px;display:flex;gap:10px}
.service-card{width:243px;height:283px;border-radius:12px;position:relative;overflow:hidden}
.service-card .photo{position:absolute;inset:0}
.service-card .label{position:absolute;bottom:16px;left:0;right:0;text-align:center;color:var(--white);font-size:15px}
.service-card .overlay{position:absolute;left:12px;right:12px;top:18px;bottom:22px;background:var(--lime);border-radius:10px;padding:18px 14px;text-align:center;color:var(--white)}
.overlay h3{font-weight:500;font-size:17px;color:#1e1e1e;margin-bottom:14px}
.overlay p{font-size:14px;line-height:1.7}
.arrow{position:absolute;width:36px;height:36px;border-radius:50%;background:#111;display:flex;align-items:center;justify-content:center}
.services .arrow{top:339px}

/* about */
.about-card{position:absolute;top:1269px;left:99px;width:1002px;height:462px;background:var(--white);border-radius:16px;box-shadow:0 4px 18px rgba(0,0,0,.15);display:flex;overflow:hidden;z-index:2}
.about-card .photo{width:489px;height:100%;background:linear-gradient(170deg,#8f9499 0%,#6e7175 35%,#7c6b58 70%,#5a4a3d 100%)}
.about-copy{padding:40px 28px 0 40px;flex:1}
.about-copy .display{font-size:23px;line-height:1.55}
.about-copy .display small{font-size:15px;letter-spacing:2px;display:block;white-space:nowrap}
.about-copy .rule{margin:14px 0 26px;width:64px}
.about-copy p{font-size:15px;line-height:1.6;color:#333;margin-bottom:18px}
.about-copy p.muted{font-size:14px;color:var(--muted)}
.tabs{display:flex;gap:14px;margin-top:12px}
.tab{width:139px;height:46px;border-radius:12px;background:var(--grey);color:var(--white);display:flex;align-items:center;justify-content:center;font-size:16px}
.tab.active{background:var(--lime)}

/* plant hire */
.plant{position:absolute;top:1624px;left:0;width:1200px;height:658px;background:var(--lime)}
.plant-copy{position:absolute;left:117px;top:196px;width:455px;color:var(--white)}
.plant-copy .display{color:var(--white);font-size:28px}
.plant-copy .rule{background:var(--white);margin:20px 0 24px}
.plant-copy p{font-size:15px;line-height:1.85}
.plant .btn{background:var(--grey);padding:13px 24px;margin-top:22px}
.plant .photo{position:absolute;left:653px;top:162px;width:432px;height:400px;border-radius:14px;background:linear-gradient(180deg,#3b6fc4 0%,#6d8b5c 30%,#9c6f4b 55%,#b58a63 100%)}

/* projects */
.projects{position:absolute;top:2282px;left:0;width:1200px;height:831px}
.projects .section-title{padding-top:120px}
.projects .rule{margin:16px auto 0}
.gallery{position:absolute;top:230px;left:124px;display:grid;grid-template-columns:repeat(4,235px);grid-auto-rows:242px;gap:4px}
.gallery .photo{width:100%;height:100%}
.projects .arrow{top:452px;background:var(--white);box-shadow:0 1px 6px rgba(0,0,0,.25);width:44px;height:44px}

/* quote */
.quote-bg{position:absolute;top:3113px;left:0;width:1200px;height:338px;background:linear-gradient(180deg,#78b23c,#86c143)}
.quote-card{position:absolute;top:3265px;left:102px;width:998px;height:590px;background:var(--white);display:flex}
.quote-form{padding:38px 0 0 42px;width:530px}
.quote-form .display{font-size:27px;line-height:1.35}
.quote-form .rule{width:96px;margin:20px 0 38px}
.field-row{display:flex;gap:18px;margin-bottom:16px}
.field{flex:1;height:44px;border:1px solid #bbb;border-radius:4px;font-size:11px;color:#777;padding:14px 12px}
.field.tall{height:112px}
.send{height:46px;background:var(--lime-dark);border-radius:6px;color:#111;font-weight:600;font-size:16px;display:flex;align-items:center;justify-content:center;margin-top:18px}
.quote-side{padding:34px 0 0 40px;flex:1}
.quote-side .photo{width:397px;height:246px;border-radius:8px;background:linear-gradient(135deg,#e9ece6,#cfe3e6 55%,#9fcfdc);box-shadow:0 2px 8px rgba(0,0,0,.15)}
.side-contacts{margin-top:30px}
.side-contacts .contact-item{border:none;padding:0 0 0 10px;margin-bottom:26px;height:auto}

/* footer */
.footer{position:absolute;top:3906px;left:0;width:1200px;height:429px;background:var(--grey);text-align:center;color:var(--white)}
.footer .name{font-family:"Michroma",sans-serif;font-size:32px;letter-spacing:2px;padding-top:100px;white-space:nowrap}
.foot-nav{display:flex;justify-content:center;gap:47px;list-style:none;font-size:20px;margin-top:44px}
.socials{display:flex;justify-content:center;gap:8px;margin-top:38px}
.socials span{width:38px;height:38px;border-radius:50%;border:2px solid var(--white)}
.copyright{font-size:14px;margin-top:40px}
</style>
</head>
<body>

<header class="topbar">
  <div class="brand">Harbourgate Earthmoving</div>
  <div class="contact-strip">
    <div class="contact-item">
      <svg viewBox="0 0 32 32" fill="none" stroke="#7cbd36" stroke-width="1.6"><path d="M8 4l5 6-3 3c2 4 5 7 9 9l3-3 6 5-3 4C16 28 4 16 4 7z"/></svg>
      <div><b>Call Us</b><span>888.888.8888</span></div>
    </div>
    <div class="contact-item">
      <svg viewBox="0 0 32 32" fill="none" stroke="#7cbd36" stroke-width="1.6"><path d="M4 13l12-9 12 9v15H4z"/><path d="M4 13l12 9 12-9"/><rect x="9" y="8" width="14" height="9"/></svg>
      <div><b>Send Us Email</b><span>info@harbourgateearthmoving.com</span></div>
    </div>
    <div class="contact-item">
      <svg viewBox="0 0 32 32" fill="none" stroke="#7cbd36" stroke-width="1.6"><path d="M16 28s-8-9-8-15a8 8 0 0116 0c0 6-8 15-8 15z"/><circle cx="16" cy="13" r="3"/><path d="M6 24l-3 5h26l-3-5"/></svg>
      <div><b>Location</b><span>358 enim ipsam voluptatem quia , Sydney</span></div>
    </div>
  </div>
</header>

<nav class="navbar">
  <ul class="nav-links">
    <li>Home</li><li>About Us</li><li>Services</li><li>Projects</li><li>Plant Hire</li><li>Contact</li>
  </ul>
  <div class="quick-quote">
    <div class="dot"><svg width="22" height="22" viewBox="0 0 32 32" fill="none" stroke="#7cbd36" stroke-width="2"><path d="M8 4l5 6-3 3c2 4 5 7 9 9l3-3 6 5-3 4C16 28 4 16 4 7z"/></svg></div>
    <div><small>Quick</small><b>Request A Quote</b></div>
  </div>
</nav>

<section class="hero">
  <div class="photo" role="img" aria-label="Photo of a pickup truck and company tipper trucks on an excavation site with an excavator behind"></div>
  <div class="hero-inner">
    <h1>Welcome To</h1>
    <div class="name">HARBOURGATE EARTHMOVING</div>
    <span class="btn">PAST PROJECTS</span>
  </div>
</section>

<section class="services">
  <h2 class="display section-title">Our <span class="accent">S</span>ervices</h2>
  <div class="rule"></div>
  <div class="arrow" style="left:83px"><svg width="12" height="12" viewBox="0 0 12 12"><path d="M8 2L4 6l4 4" stroke="#fff" stroke-width="1.5" fill="none"/></svg></div>
  <div class="service-row">
    <div class="service-card">
      <div class="photo" role="img" aria-label="Photo of a conveyor tower over bulk earth stockpiles" style="background:linear-gradient(180deg,#7f95ad,#7a5f4a 60%,#8a5a3a)"></div>
      <div class="label">BULK EXCAVATION</div>
    </div>
    <div class="service-card">
      <div class="photo" role="img" aria-label="Photo of workers in hard hats on a detailed excavation site" style="background:linear-gradient(180deg,#c98a2b,#6c5a48)"></div>
      <div class="overlay">
        <h3>DETAILED EXCAVATION</h3>
        <p>Sed ut perspiciatis unde omnis iste natus error sit voluptatem accusantium doloremque laudantium, accusantium doloremque laudantium,</p>
      </div>
    </div>
    <div class="service-card">
      <div class="photo" role="img" aria-label="Photo of an excavator in demolition rubble" style="background:linear-gradient(180deg,#6a5f55,#8b6f55 50%,#5a4a3c)"></div>
      <div class="label">DEMOLITION</div>
    </div>
    <div class="service-card">
      <div class="photo" role="img" aria-label="Photo of a shored excavation beside houses" style="background:linear-gradient(180deg,#9aa5ae,#7d7a70 50%,#5c5549)"></div>
      <div class="label">SHORING</div>
    </div>
  </div>
  <div class="arrow" style="left:1085px"><svg width="12" height="12" viewBox="0 0 12 12"><path d="M4 2l4 4-4 4" stroke="#fff" stroke-width="1.5" fill="none"/></svg></div>
</section>

<section class="about-card">
  <div class="photo" role="img" aria-label="Photo of excavators and a company truck on a demolition site"></div>
  <div class="about-copy">
    <h2 class="display"><span class="accent">A</span>bout <span class="accent">U</span>s<small>Harbourgate Earthmoving</small></h2>
    <div class="rule"></div>
    <p>Sed ut perspiciatis unde omnis iste natus error sit voluptatem accusantium doloremque laudantium, totam rem aperiam, eaque ipsa quae ab illo inventore veritatis et quasi architecto beatae vitae dicta sunt explicabo.</p>
    <p class="muted">Sed ut perspiciatis unde omnis iste natus error sit voluptatem accusantium doloremque laudantium, totam rem aperiam, eaque ipsa quae ab illo inventore veritatis et quasi architecto beatae vitae dicta sunt explicabo.</p>
    <div class="tabs"><span class="tab active">TEAM STORY</span><span class="tab">MISSION</span><span class="tab">SAFETY</span></div>
  </div>
</section>

<section class="plant">
  <div class="plant-copy">
    <h2 class="display">Plant Hire</h2>
    <div class="rule"></div>
    <p>Sed ut perspiciatis unde omnis iste natus error sit voluptatem accusantium doloremque laudantium, totam rem aperiam, eaque ipsa quae ab illo inventore veritatis et quasi architecto beatae vitae dicta sunt explicabo. Nemo enim ipsam voluptatem quia voluptas sit aspernatur aut odit aut fugit, sed quia consequuntur magni dolores eos qui ratione voluptatem sequi nesciunt. Neque porro quisquam est, qui dolorem ipsum quia dolor sit amet, consectetur</p>
    <span class="btn">VIEW MORE</span>
  </div>
  <div class="photo" role="img" aria-label="Photo of a deep residential excavation with an excavator under blue sky"></div>
</section>

<section class="projects">
  <h2 class="display section-title"><span class="accent">P</span>rojects</h2>
  <div class="rule"></div>
  <div class="arrow" style="left:99px"><svg width="12" height="12" viewBox="0 0 12 12"><path d="M8 2L4 6l4 4" stroke="#555" stroke-width="1.5" fill="none"/></svg></div>
  <div class="gallery">
    <div class="photo" role="img" aria-label="Photo of a levelled site with track marks" style="background:linear-gradient(180deg,#7f8d95,#8a7562 40%,#6c5846)"></div>
    <div class="photo" role="img" aria-label="Photo of a conveyor gantry over a quarry" style="background:linear-gradient(180deg,#8d9aa0,#5d6258 60%,#4c4a44)"></div>
    <div class="photo" role="img" aria-label="Photo of a crew in orange workwear laying membrane" style="background:linear-gradient(180deg,#8aa4bc,#8a6a4e 50%,#b5532e)"></div>
    <div class="photo" role="img" aria-label="Photo of a yellow excavator beside buildings" style="background:linear-gradient(180deg,#9aa9b4,#b59135 50%,#6f5a3f)"></div>
    <div class="photo" role="img" aria-label="Photo of excavators in front of apartment blocks" style="background:linear-gradient(180deg,#a7aeb2,#8f7a63 55%,#6b5641)"></div>
    <div class="photo" role="img" aria-label="Photo of a muddy cleared site with water pools" style="background:linear-gradient(180deg,#8b939a,#6c6253 50%,#5b5347)"></div>
    <div class="photo" role="img" aria-label="Photo of demolition rubble inside a building" style="background:linear-gradient(180deg,#6b5a4c,#7e6b5c 50%,#5f5148)"></div>
    <div class="photo" role="img" aria-label="Photo of an excavator among trees on a site" style="background:linear-gradient(180deg,#6e7f5a,#a48d3e 55%,#5a4c3a)"></div>
  </div>
  <div class="arrow" style="left:1047px"><svg width="12" height="12" viewBox="0 0 12 12"><path d="M4 2l4 4-4 4" stroke="#555" stroke-width="1.5" fill="none"/></svg></div>
</section>

<div class="quote-bg" role="img" aria-label="Green tinted photo of an earthworks site"></div>
<section class="quote-card">
  <div class="quote-form">
    <h2 class="display"><span class="accent">G</span>et <span class="accent">A</span><br><span class="accent">F</span>ree <span class="accent">Q</span>uote</h2>
    <div class="rule"></div>
    <div class="field-row"><div class="field">Full Name</div><div class="field">Email</div></div>
    <div class="field-row"><div class="field">Phone</div><div class="field">Zip Code</div></div>
    <div class="field-row"><div class="field">Service</div></div>
    <div class="field-row"><div class="field tall">Message</div></div>
    <div class="send">Send Message</div>
  </div>
  <div class="quote-side">
    <div class="photo" role="img" aria-label="Map of Sydney showing the office location"></div>
    <div class="side-contacts">
      <div class="contact-item">
        <svg viewBox="0 0 32 32" fill="none" stroke="#7cbd36" stroke-width="1.6"><path d="M8 4l5 6-3 3c2 4 5 7 9 9l3-3 6 5-3 4C16 28 4 16 4 7z"/></svg>
        <div><b>Call Us</b><span>888.888.8888</span></div>
      </div>
      <div class="contact-item">
        <svg viewBox="0 0 32 32" fill="none" stroke="#7cbd36" stroke-width="1.6"><path d="M4 13l12-9 12 9v15H4z"/><path d="M4 13l12 9 12-9"/><rect x="9" y="8" width="14" height="9"/></svg>
        <div><b>Send Us Email</b><span>info@harbourgateearthmoving.com</span></div>
      </div>
      <div class="contact-item">
        <svg viewBox="0 0 32 32" fill="none" stroke="#7cbd36" stroke-width="1.6"><path d="M16 28s-8-9-8-15a8 8 0 0116 0c0 6-8 15-8 15z"/><circle cx="16" cy="13" r="3"/><path d="M6 24l-3 5h26l-3-5"/></svg>
        <div><b>Location</b><span>358 enim ipsam voluptatem quia , Sydney</span></div>
      </div>
    </div>
  </div>
</section>

<footer class="footer">
  <div class="name">HARBOURGATE EARTHMOVING</div>
  <ul class="foot-nav"><li>Home</li><li>About Us</li><li>Services</li><li>Projects</li><li>Plant Hire</li><li>Contact</li></ul>
  <div class="socials"><span></span><span></span><span></span><span></span><span></span></div>
  <p class="copyright">Copyright 2025. Company Name. All Rights Reserved</p>
</footer>

</body>
</html>
```